Tendril Harbor

Our product is a subscription-based website for doctors and medical practices. It allows contract-based doctors (locums) to book jobs with medical practices and to organise their own finances (invoicing, pension, etc). Also, it allows medical practices to post jobs, and book locums.

We need a website design that looks clean and professional. It should look easy-to-use and friendly, which will encourage users to sign up as they'll hopefully think using the system will also be simple and friendly.

As well as the homepage, we need a design for the logged-in view. This is very different to the website but equally important. It needs to be very functional. Much more like an application and less like a website.

PLEASE SUBMIT BOTH WEBSITE HOMEPAGE DESIGN AND APPLICATION DASHBOARD DESIGN.

The application is built and we already have a user interface (linked below) so we're not looking for a designer to decide what is on these pages - we already have that. We're ONLY asking for visual design. Please just make the content we have look good. You may move parts of the content around a small amount but the functionality is very much signed off now so it's only visual styling that we need addressed.

Please base the branding around the current logo, which can't be changed. You can get the logo as an EPS here : http://clients.brassowl.co.uk/tendrilharbor/design/logo-green.eps

Here is a link to the current design for the website, and for the application dashboard:
http://clients.brassowl.co.uk/tendrilharbor/design/

Also, here is a video we've had made which might help you with the brand:
http://quivlo.com/71825364
Updates

Just in case it isn't clear, the video (linked in the main brief) is an essential part of the website homepage.

Reason: We need to spend some time looking over these designs and might ask for a few amendments to one or two in the next few days. Thanks.

Target Market(s)

Doctors and medical practices

Industry/Entity Type

Medical

Requirements
Must have
• It must have all the features that are in the linked designs - homepage and dashboard.

```html
<!DOCTYPE html>
<html lang="en">
<head>
<meta charset="utf-8">
<title>Tendril Harbor</title>
<link rel="stylesheet" href="https://fonts.googleapis.com/css2?family=Arimo:ital,wght@0,400;0,700;1,400&display=swap">
<style>
:root{
  --sky:#e3f0f8;
  --sky-deep:#c9e2f2;
  --panel:#f4f9fd;
  --line:#b9d6ea;
  --blue:#1b6aa6;
  --blue-dark:#0e4c82;
  --navy:#0b3f6e;
  --green:#3b9b2f;
  --green-dark:#2b7a22;
  --text:#2c3b48;
  --muted:#5d6f7e;
  --white:#ffffff;
}
*{box-sizing:border-box;margin:0;padding:0}
html,body{width:786px;height:1200px;overflow:hidden}
body{font-family:"Arimo",Arial,sans-serif;color:var(--text);background:linear-gradient(var(--sky-deep),var(--sky) 300px,var(--sky));font-size:11px;position:relative}
.account{position:absolute;left:10px;top:8px;display:flex;gap:8px;align-items:center}
.account .who{background:var(--blue-dark);color:var(--white);font-size:10px;padding:3px 8px;border-radius:3px;line-height:1.3}
.account .who small{display:block;font-size:9px;opacity:.8}
.account a{color:var(--blue-dark);font-size:10px}
.brand{position:absolute;left:22px;top:96px;display:flex;align-items:center;gap:12px}
.brand .dot{width:54px;height:54px;border-radius:50%;background:var(--green)}
.brand .name{font-size:34px;font-weight:700;color:var(--blue);line-height:1}
.brand .tag{font-size:13px;color:var(--green);margin-top:4px}
.promo{position:absolute;left:404px;top:12px;width:372px;height:186px;border-radius:6px;background:linear-gradient(#47a83a,#2c8426);color:var(--white);overflow:hidden;border:2px solid var(--white)}
.promo h2{position:absolute;left:14px;top:12px;width:210px;font-size:16px;line-height:1.2}
.promo ul{position:absolute;left:14px;top:66px;list-style:none;font-size:11.5px;line-height:19px}
.promo li::before{content:"";display:inline-block;width:7px;height:7px;background:var(--white);border-radius:50%;margin-right:7px}
.promo .photo{position:absolute;right:0;top:0;width:140px;height:160px;background:linear-gradient(135deg,#bcdcef,#e9f3f9 60%,#8fb9d2)}
.promo .cta{position:absolute;left:0;right:0;bottom:0;height:26px;background:var(--blue-dark);text-align:right;padding:6px 14px;font-weight:700;font-size:12px}
nav{position:absolute;left:10px;top:196px;width:766px;height:24px;background:linear-gradient(#2f82c0,var(--blue-dark));border-radius:3px;display:flex;padding-left:8px}
nav a{color:var(--white);text-decoration:none;font-size:11px;padding:0 16px;line-height:24px;border-right:1px solid rgba(255,255,255,.35)}
nav a.on{background:var(--white);color:var(--blue-dark);border-radius:3px 3px 0 0;margin-top:3px;line-height:21px}
.audiences{position:absolute;left:10px;top:232px;width:766px;display:flex;gap:14px}
.audience{flex:1;height:316px;background:var(--panel);border:1px solid var(--line);border-radius:5px;overflow:hidden}
.audience header{background:linear-gradient(#dcecf7,#c3ddef);padding:10px 14px 8px}
.audience h3{color:var(--blue);font-size:17px}
.audience header p{color:var(--blue-dark);font-size:12px}
.steps{list-style:none;padding:10px 14px 0}
.steps li{display:flex;gap:9px;margin-bottom:12px}
.steps .num{flex:none;width:17px;height:17px;border-radius:50%;background:var(--green);color:var(--white);font-size:10px;font-weight:700;text-align:center;line-height:17px}
.steps b{display:block;color:var(--blue-dark);font-size:11.5px;margin-bottom:2px}
.steps span{font-size:10px;color:var(--muted);line-height:1.35;display:block}
.audience footer{display:flex;align-items:center;gap:20px;padding:4px 14px}
.btn{background:linear-gradient(#5bb64a,var(--green-dark));color:var(--white);font-weight:700;font-size:12px;padding:7px 18px;border-radius:4px}
.more{font-size:10px;color:var(--blue-dark);text-align:center;line-height:1.3}
.more b{display:block}
.trial{position:absolute;left:10px;top:556px;width:766px;height:236px;display:flex;gap:12px}
.signup{flex:0 0 506px;background:var(--panel);border:1px solid var(--line);border-radius:5px;overflow:hidden}
.tabs{display:flex;gap:3px;padding:6px 8px 0;background:#cfe4f3}
.tabs span{background:var(--blue-dark);color:var(--white);font-size:9.5px;padding:4px 9px;border-radius:3px 3px 0 0}
.signup form{padding:10px 14px}
.signup .lead{color:var(--blue-dark);font-size:12px;margin-bottom:8px}
.role{font-size:10.5px;margin-bottom:8px;display:flex;gap:12px}
.fields{display:grid;grid-template-columns:170px 170px;gap:4px 40px}
.fields label{font-size:10px;color:var(--blue-dark)}
.fields .box{height:18px;border:1px solid var(--line);background:var(--white);margin-bottom:6px}
.agree{font-size:10px;margin-top:8px;display:flex;align-items:center;gap:6px}
.agree i{width:10px;height:10px;border:1px solid var(--muted);background:var(--white)}
.agree b{color:var(--blue-dark)}
.video{flex:1;background:var(--panel);border:1px solid var(--line);border-radius:5px;padding:10px}
.video p{color:var(--blue-dark);font-size:11.5px;line-height:1.35;margin-bottom:8px}
.player{position:relative;height:158px;background:linear-gradient(#f3f8fb,#cfe3f0);border:1px solid var(--line)}
.player .bar{position:absolute;left:0;right:0;bottom:0;height:16px;background:#2f3d48}
.press{position:absolute;left:10px;top:800px;width:766px;height:130px;background:var(--panel);border:1px solid var(--line);border-radius:5px;display:flex;padding:18px 20px;gap:26px}
.press div{flex:1}
.press strong{display:block;font-size:23px;color:#1f2a33;margin-bottom:8px}
.press p{font-size:10px;color:var(--muted);line-height:1.4}
.quotes{position:absolute;left:10px;top:940px;width:766px;display:flex;gap:14px}
.quotes blockquote{flex:1;text-align:center;font-size:10.5px;line-height:1.45;padding:8px 16px;border-top:2px solid var(--line)}
.quotes cite{display:block;font-weight:700;font-style:italic;margin-top:4px;color:var(--blue-dark)}
.site-foot{position:absolute;left:0;top:1050px;width:786px;height:150px;background:var(--navy);color:var(--white);font-size:10px;padding:14px 24px;display:flex;gap:60px}
.site-foot ul{list-style:none;line-height:18px}
.site-foot li::before{content:"";display:inline-block;width:5px;height:5px;background:var(--green);margin-right:7px}
.site-foot .info{line-height:16px;flex:1}
.site-foot .legal{position:absolute;right:24px;bottom:14px;display:flex;gap:10px}
</style>
</head>
<body>
<div class="account"><div class="who">Mrs. Harriet Moss<small>Go to Dashboard</small></div><a href="#">Sign out</a></div>

<div class="brand"><div class="dot"></div><div><div class="name">Tendril Harbor</div><div class="tag">Get connected. Stay organised.</div></div></div>

<section class="promo">
  <h2>A Network for Connecting Locums with Employers</h2>
  <ul><li>Better connectivity</li><li>More choice</li><li>Less paperwork</li><li>Lower costs</li></ul>
  <div class="photo" role="img" aria-label="Photo of smiling doctors"></div>
  <div class="cta">Sign up for free-try us out</div>
</section>

<nav><a class="on" href="#">Home</a><a href="#">Locums</a><a href="#">Employers</a><a href="#">Pricing</a><a href="#">About us</a><a href="#">FAQ</a><a href="#">Contact us</a></nav>

<div class="audiences">
  <article class="audience">
    <header><h3>GP Locums</h3><p>The complete platform to organize your locum life</p></header>
    <ul class="steps">
      <li><span class="num">1</span><div><b>Find Jobs</b><span>Search, apply and get invited for a wide selection of jobs from practices and agencies.</span></div></li>
      <li><span class="num">2</span><div><b>Find Jobs</b><span>Profile, diary management, invoicing, pension forms, finances, tax returns.</span></div></li>
      <li><span class="num">3</span><div><b>Find Jobs</b><span>Create your online profile and connect with your own network of employers allowing you to automatically fill jobs.</span></div></li>
    </ul>
    <footer><span class="btn">Sign up</span><span class="more">More about<b>Tendril Harbor for locums</b></span></footer>
  </article>
  <article class="audience">
    <header><h3>Employers</h3><p>One-stop solution for your locum needs</p></header>
    <ul class="steps">
      <li><span class="num">1</span><div><b>Find Jobs</b><span>Post your locum requirements. Search and employ the right locums via your e-booking system.</span></div></li>
      <li><span class="num">2</span><div><b>Find Jobs</b><span>Profile, locum rota management, pre-employment checks, locum market statistics.</span></div></li>
      <li><span class="num">3</span><div><b>Find Jobs</b><span>Create your online profile and connect with your own network of locums allowing them to automatically fill jobs.</span></div></li>
    </ul>
    <footer><span class="btn">Sign up</span><span class="more">More about<b>Tendril Harbor for employers</b></span></footer>
  </article>
</div>

<div class="trial">
  <section class="signup">
    <div class="tabs"><span>"The network" for locums and employers</span><span>Save time and cost</span><span>Try it free now</span></div>
    <form>
      <p class="lead">Try it now with just an email address, GMC number and password!</p>
      <div class="role"><span>I am ◉ a locum</span><span>○ an employer</span></div>
      <div class="fields">
        <div><label>Email</label><div class="box"></div></div>
        <div><label>GMC number</label><div class="box"></div></div>
        <div><label>Password</label><div class="box"></div></div>
        <div><label>Confirm Password</label><div class="box"></div></div>
      </div>
      <p class="agree"><i></i>I agree to the <b>terms of services</b> and the <b>privacy policy</b></p>
    </form>
  </section>
  <aside class="video">
    <p>Watch our Video to Learn more about Tendril Harbor.</p>
    <div class="player" role="img" aria-label="Brand video still">
      <svg width="240" height="158" viewBox="0 0 240 158" style="position:absolute;left:0;top:0"><circle cx="120" cy="70" r="18" fill="#0e4c82" opacity=".8"/><path d="M114 60 L130 70 L114 80Z" fill="#fff"/></svg>
      <div class="bar"></div>
    </div>
  </aside>
</div>

<section class="press">
  <div><strong>Daily Ledger</strong><p>A simple way for locum doctors and practices to meet, book and settle work without fuss.</p></div>
  <div><strong>civicpost.co.uk</strong><p>Takes the paperwork out of locum life and lets doctors focus on their patients again.</p></div>
  <div><strong>Morning Courier</strong><p>Practices report filling sessions faster and spending less on agency fees each month.</p></div>
</section>

<div class="quotes">
  <blockquote>So easy to set up. Five minutes and you're in. And it does all the boring admin stuff that I hate.<cite>Name of Person, Locum</cite></blockquote>
  <blockquote>As a practice, it's great to be able to find locums quickly and easily. No more time-consuming agency phone calls!<cite>Brindle Medical Centre</cite></blockquote>
</div>

<footer class="site-foot">
  <ul><li>Home</li><li>Locums</li><li>Employers</li><li>About us</li><li>FAQ</li><li>Contact us</li></ul>
  <div class="info"><p>We're here to help: support@tendrilharbor.co.uk</p><br><p>Copyright © 2013 Tendril Harbor Ltd. All Rights Reserved</p><p>Registered in England no. 08412375</p></div>
  <div class="legal"><span>Terms of service</span><span>|</span><span>Privacy policy</span><span>|</span><span>Refund policy</span></div>
</footer>
</body>
</html>
```